Steadfast Care - Need Stationary Design

We need a stationary pack for our new Care company based in the uk
Are corporate colours are Pink and purple
Please use attached logo
Target Market(s)
The Care Industry
Industry/Entity Type
It Company
Contact Information for Business Card
Melissa Rowden
Director

```html
<!DOCTYPE html>
<html lang="en">
<head>
<meta charset="utf-8">
<title>Steadfast Care – Envelope</title>
<link href="https://fonts.googleapis.com/css2?family=Open+Sans:wght@400;700&display=swap" rel="stylesheet">
<style>
  :root {
    --backdrop: #b5a27f;
    --paper: #f5f4f3;
    --purple: #8a5db0;
    --purple-light: #b07ed6;
    --pink: #e83e9c;
    --pink-soft: #d97fb3;
    --ink: #4a4a4a;
    --faint: #f1dde9;
  }
  html, body {
    margin: 0;
    width: 1200px;
    height: 1122px;
    overflow: hidden;
    background: var(--backdrop);
    font-family: "Open Sans", sans-serif;
  }
  .canvas { position: relative; width: 1200px; height: 1122px; }
  .envelope {
    position: absolute;
    background: var(--paper);
    overflow: hidden;
  }
  .envelope-back { left: 56px; top: 75px; width: 1050px; height: 478px; }
  .envelope-front { left: 53px; top: 591px; width: 1056px; height: 481px; }
  .flap { position: absolute; left: 0; top: 0; }
  .flap-brand {
    position: absolute;
    top: 62px; left: 0; width: 100%;
    display: flex; justify-content: center; align-items: center; gap: 12px;
    color: #fff; font-size: 26px; font-weight: 400;
  }
  .brand-dot { width: 22px; height: 22px; border-radius: 50%; background: currentColor; }
  .sender { position: absolute; left: 40px; top: 58px; }
  .sender-brand {
    display: flex; align-items: center; gap: 10px;
    color: var(--purple); font-size: 22px; margin-left: 30px;
  }
  .sender-brand .brand-dot { background: var(--pink); width: 26px; height: 26px; }
  .sender-company {
    margin: 30px 0 0 65px; font-size: 16px; font-weight: 700; color: var(--ink);
  }
  .sender-address { margin: 4px 0 0 40px; font-size: 16px; line-height: 22px; color: var(--ink); }
  .sender-address span { display: block; }
  .sender-address span + span { margin-left: 14px; }
  .watermark {
    position: absolute; left: 690px; top: 40px;
    width: 300px; height: 300px; border-radius: 50%;
    background: var(--faint); opacity: .7;
  }
  .wave { position: absolute; left: 0; bottom: 0; }
</style>
</head>
<body>
<div class="canvas">
  <section class="envelope envelope-back">
    <svg class="flap" width="1050" height="175" viewBox="0 0 1050 175" aria-hidden="true">
      <path d="M0 0 H1050 L1030 110 Q1020 175 955 175 H95 Q30 175 20 110 Z" fill="var(--purple)"/>
    </svg>
    <div class="flap-brand"><span class="brand-dot"></span><span>Steadfast Care</span></div>
  </section>

  <section class="envelope envelope-front">
    <div class="watermark"></div>
    <div class="sender">
      <div class="sender-brand"><span class="brand-dot"></span><span>Steadfast Care</span></div>
      <div class="sender-company">STEADFAST CARE LTD</div>
      <div class="sender-address">
        <span>4 Alder Court 18 Mill Lane</span>
        <span>Thornbury Glos BS35 4QX</span>
      </div>
    </div>
    <svg class="wave" width="1056" height="110" viewBox="0 0 1056 110" aria-hidden="true">
      <path d="M0 30 Q300 60 600 35 T1056 12 V110 H0 Z" fill="var(--purple-light)"/>
      <path d="M0 48 Q320 70 620 45 T1056 30 V110 H0 Z" fill="var(--pink-soft)"/>
      <path d="M0 55 Q320 74 620 52 T1056 40" fill="none" stroke="#fff" stroke-width="3"/>
      <path d="M0 62 Q320 82 620 60 T1056 46" fill="none" stroke="var(--pink)" stroke-width="6"/>
      <path d="M0 70 Q320 90 620 68 T1056 55 V110 H0 Z" fill="var(--purple)"/>
      <path d="M0 69 Q320 89 620 67 T1056 54" fill="none" stroke="#fff" stroke-width="2"/>
    </svg>
  </section>
</div>
</body>
</html>
```